Design a new product for a successful cannabis company

We need a package design for a new brand. We are a large cannabis company near Seattle, USA. The name of the product is called the "Bellwyn Rook". It is a pure cannabis oil extract that is used through a magnetic vaporizer cartridge. We need a graphic template designed that will be printed on a card and inserted into the plastic packaging. This project is design the overall concept, and we will add the required warnings on our end once a design is chosen.

Dimensions:
Width - 2.5625 inches
Height - 3.3125 inches
Viewing Window Width - .4375 inches
Viewing Window Height - 2.0 Inches
Distance from the bottom of the card to the viewing window- .4375 inches
Distance from the left side to the viewing window - 1.0625 inch
Distance from the right side to the viewing window - 1.0625 inch

Theme:
- We would like it to have some sort of Bellwyn Rook historical feel. I attached the dimensions for size reference. Please extract that "BellwynRook" text/font if possible. We really want to use that.
- You could use an old map from that region and time in history.
- Wiki link explaining the Bellwyn Rook (https://docs.quorvel-archive.org/page/Bellwyn_Rook)

Additional Notes:
- There is an area where the physical cartridge will go. Feel free to extend the background into that area but please do not place any text there.
- There is a backside of this package that customers will see. We will place our warning text back there along with a product description. Please keep the back side clear of text but have it match whatever color scheme or background you do on the front side.
- I included an example of a competitor using the same package shape. That's what it will be printed on

Please reach out if you have questions or need clarification. I will be adding details as we go to help with the concept. Thank you!

Target Market(s)

Cannabis oil users of all ages

Colors

Designer to choose colors to be used in the design.

Requirements
Must have
• The same BellwynRook text from the attached concert poster
• Must say "A magnetic vape cartridge."
Nice to have
• A historical feel by faintly using an 12th century English map as the background. Open to anything in order to achieve a classic feel.
Should not have
• Bright colors

```html
<!DOCTYPE html>
<html lang="en">
<head>
<meta charset="utf-8">
<title>Bellwyn Rook – Cartridge Card</title>
<link href="https://fonts.googleapis.com/css2?family=Righteous&family=Quicksand:wght@500;600;700&display=swap" rel="stylesheet">
<style>
  :root {
    --page: #ffffff;
    --parchment-light: #f2e6c8;
    --parchment-mid: #dcc79c;
    --parchment-dark: #a68a5f;
    --edge: #2b2420;
    --oxblood: #6b0f12;
    --ink-brown: #4a3f36;
    --label-white: #ffffff;
  }
  html, body {
    margin: 0;
    padding: 0;
    width: 1094px;
    height: 1200px;
    overflow: hidden;
    background: var(--page);
  }
  .canvas {
    position: relative;
    width: 1094px;
    height: 1200px;
  }
  /* Card: 2.5625 × 3.3125 in at ~196.5 px/in */
  .card {
    position: absolute;
    left: 264px;
    top: 246px;
    width: 503px;
    height: 652px;
    border: 1.5px solid var(--edge);
    border-radius: 22px;
    overflow: hidden;
    box-sizing: border-box;
  }
  .card__map {
    position: absolute;
    inset: 0;
    background:
      radial-gradient(ellipse at 72% 38%, var(--parchment-light) 0%, rgba(242,230,200,0) 55%),
      radial-gradient(ellipse at 30% 85%, rgba(166,138,95,0.55) 0%, rgba(166,138,95,0) 60%),
      radial-gradient(ellipse at 20% 10%, rgba(166,138,95,0.6) 0%, rgba(166,138,95,0) 45%),
      linear-gradient(160deg, var(--parchment-mid) 0%, var(--parchment-light) 45%, var(--parchment-mid) 100%);
  }
  /* Window: 0.4375 × 2.0 in, centred, 0.4375 in from bottom */
  .card__window {
    position: absolute;
    left: 207px;
    top: 171px;
    width: 86px;
    height: 393px;
    border: 1.5px solid var(--edge);
    border-radius: 8px;
    box-sizing: border-box;
  }
  .brand {
    position: absolute;
    left: 0;
    top: 34px;
    width: 100%;
    margin: 0;
    text-align: center;
    white-space: nowrap;
    font-family: "Righteous", sans-serif;
    font-weight: 400;
    font-size: 54px;
    line-height: 1;
    color: var(--oxblood);
    text-transform: uppercase;
    letter-spacing: -1px;
  }
  .brand-rule {
    position: absolute;
    left: 40px;
    top: 104px;
    width: 421px;
    height: 3px;
    background: var(--oxblood);
  }
  .tagline {
    position: absolute;
    left: 0;
    top: 118px;
    width: 100%;
    margin: 0;
    text-align: center;
    white-space: nowrap;
    font-family: "Quicksand", sans-serif;
    font-weight: 600;
    font-size: 23px;
    line-height: 1.1;
    color: var(--ink-brown);
    text-transform: uppercase;
    letter-spacing: -0.3px;
  }
  .maker {
    position: absolute;
    left: 310px;
    top: 320px;
    width: 178px;
    margin: 0;
    text-align: center;
    font-family: "Quicksand", sans-serif;
    font-weight: 500;
    font-size: 23px;
    line-height: 1.2;
    color: var(--oxblood);
    text-transform: uppercase;
    letter-spacing: -0.4px;
  }
  .compat {
    position: absolute;
    left: 0;
    top: 590px;
    width: 100%;
    margin: 0;
    text-align: center;
    white-space: nowrap;
    font-family: "Quicksand", sans-serif;
    font-weight: 700;
    font-size: 14px;
    color: var(--label-white);
    text-transform: uppercase;
    -webkit-text-stroke: 2px var(--ink-brown);
    paint-order: stroke fill;
  }
</style>
</head>
<body>
  <main class="canvas">
    <section class="card">
      <div class="card__map" role="img" aria-label="Aged parchment map of the British Isles in sepia tones"></div>
      <div class="card__window" aria-hidden="true"></div>

      <h1 class="brand">Bellwyn Rook</h1>
      <div class="brand-rule"></div>

      <p class="tagline">A Magnetic Vape Cartridge”</p>

      <p class="maker">A Harbor Ridge Product</p>

      <p class="compat">For use with most magnetic batteries</p>
    </section>
  </main>
</body>
</html>
```